Boldmere Nutrition: Premium Sports Nutrition (Package Design)

We are a Premium Sports Nutrition Company, looking at nutrition needs of outdoor athletes in focus.
We Need Packaging for our Protein Product, called 1. Protein: Recovery
Flavour: Mild Chocolate
and 2. Vimtrax: Summit

The Packaging should be Premium, Should look like an upmarket product
but should not look as an artificial or synthetic product.
Should look like a consumable product which people will consume and looks safe to consume.
At the same time, should look very eye catching and get attention of the people.
User Friendly Yet Premium and Elegant Design.

We would like to go for a single colour as Base.
The Logo should Sync in well with the package.
The content text should be simple not much bold.

The design can include sports icon, including Cycling,Swimming,Running,Gymming,Hockey as a must if applied.
These should be placed on the top of the packaging

This packaging is required for sachets and cardboard boxes, plastic boxes, thus designers are required to send all three.

Sachets are expected to be 170mm tall and 108mm wide, single serve stand up sachet pouch.

All designers to send packaging of all of these in
1. Sachet Base Colour (1. Matte White 2. Matte Black)
2. Plastic Boxes
3. Cardboard Box to keep the sachets in it
Updates

We are still looking for more options!

Target Market(s)

Sports Nutrition, Gym Goers, Outdoor Athletes, Cyclists, Runners, Triathletes, Swimmers, Hockey, Cricket Players

Industry/Entity Type

Nutrition

Font styles to use
Sans Serif

Requirements
Must have
• Sync in well with the Logo
• Should Blend well with Matte White Colour as Base of the Sachet

```html
<!DOCTYPE html>
<html lang="en">
<head>
<meta charset="utf-8">
<title>Boldmere Nutrition – Protein: Recovery</title>
<link href="https://fonts.googleapis.com/css2?family=Exo+2:ital,wght@0,600;1,500&family=Share+Tech+Mono&family=Saira+Condensed:wght@800&family=Yanone+Kaffeesatz:wght@500;700&display=swap" rel="stylesheet">
<style>
  :root {
    --page-bg: #e6e6ea;
    --pack-black: #060607;
    --shield-edge: #26262a;
    --brand-blue: #1f8fe0;
    --tag-blue: #2c6fd6;
    --lime: #b8e04a;
    --cyan: #22a8ef;
    --mild-yellow: #e8d43a;
    --choc: #c8622c;
    --choc-soft: #a0543a;
  }
  * { margin: 0; padding: 0; box-sizing: border-box; }
  html, body { width: 1200px; height: 960px; overflow: hidden; background: var(--page-bg); }

  .pack-front {
    position: absolute; left: 320px; top: 20px;
    width: 560px; height: 920px;
    background: var(--pack-black);
    overflow: hidden;
    box-shadow: 0 6px 24px rgba(0,0,0,.25);
  }

  .sport-scene {
    position: absolute; left: 0; top: 300px; width: 560px; height: 330px;
    background:
      radial-gradient(ellipse 45% 55% at 52% 78%, rgba(225,225,230,.75), transparent 70%),
      radial-gradient(ellipse 30% 60% at 12% 55%, rgba(160,160,165,.55), transparent 70%),
      radial-gradient(ellipse 30% 60% at 88% 60%, rgba(150,150,155,.5), transparent 70%),
      linear-gradient(180deg, #1c1c1f 0%, #55555a 55%, #2a2a2d 100%);
  }
  .lower-field {
    position: absolute; left: 0; top: 630px; width: 560px; height: 290px;
    background:
      radial-gradient(ellipse 35% 40% at 30% 20%, rgba(120,120,125,.35), transparent 70%),
      radial-gradient(ellipse 30% 45% at 80% 55%, rgba(110,110,115,.3), transparent 70%),
      linear-gradient(180deg, #232326 0%, #121214 60%, var(--pack-black) 100%);
  }

  .pack-front svg.shield { position: absolute; left: 0; top: 0; }

  .brand { position: absolute; left: 0; right: 0; top: 178px; text-align: center; }
  .brand-name {
    display: inline-flex; align-items: center; gap: 10px;
    font-family: "Exo 2", sans-serif; font-weight: 600;
    font-size: 29px; line-height: 1; color: var(--brand-blue);
    padding-bottom: 5px; border-bottom: 1px solid var(--tag-blue);
  }
  .brand-mark { width: 16px; height: 16px; border-radius: 50%; background: var(--brand-blue); }
  .brand-tagline {
    margin-top: 5px;
    font-family: "Exo 2", sans-serif; font-style: italic; font-weight: 500;
    font-size: 12px; letter-spacing: 2.4px; color: var(--tag-blue);
  }

  .product { position: absolute; left: 0; right: 0; top: 338px; text-align: center; }
  .product-name {
    font-family: "Share Tech Mono", monospace; font-size: 37px;
    letter-spacing: 3px; color: var(--lime); line-height: 1;
  }
  .product-variant {
    margin-top: 8px;
    font-family: "Saira Condensed", sans-serif; font-weight: 800;
    font-size: 38px; letter-spacing: 1px; color: var(--cyan); line-height: 1;
  }

  .flavour { position: absolute; left: 200px; top: 640px; width: 200px; height: 120px; }
  .flavour-with {
    position: absolute; left: 0; top: 0;
    font-family: "Yanone Kaffeesatz", sans-serif; font-weight: 500;
    font-size: 18px; color: #d8d8da;
  }
  .flavour-mild {
    position: absolute; left: 64px; top: 8px;
    font-family: "Yanone Kaffeesatz", sans-serif; font-weight: 700;
    font-size: 22px; color: var(--mild-yellow);
    border-bottom: 2px solid var(--mild-yellow); line-height: 1;
  }
  .flavour-name {
    position: absolute; left: -8px; top: 30px;
    font-family: "Yanone Kaffeesatz", sans-serif; font-weight: 700;
    font-size: 76px; line-height: 1; color: var(--choc);
    text-shadow: 0 2px 0 #5a2410;
  }
</style>
</head>
<body>
  <main class="pack-front">
    <div class="sport-scene" role="img" aria-label="Monochrome action scene with silhouettes of a hockey player, swimmer, cyclist, push-up athlete and runner"></div>
    <div class="lower-field" role="img" aria-label="Dark misty backdrop with a faded sprinting athlete"></div>

    <svg class="shield" width="560" height="920" viewBox="0 0 560 920" aria-hidden="true">
      <defs>
        <linearGradient id="shieldFill" x1="0" y1="0" x2="0" y2="1">
          <stop offset="0" stop-color="#040405"/>
          <stop offset="1" stop-color="#0f0f12"/>
        </linearGradient>
      </defs>
      <polygon points="55,0 513,0 513,300 293,555 55,300" fill="url(#shieldFill)" stroke="var(--shield-edge)" stroke-width="3"/>
    </svg>

    <header class="brand">
      <div class="brand-name"><span class="brand-mark"></span>Boldmere Nutrition</div>
      <div class="brand-tagline">PREMIUM SPORTS NUTRITION</div>
    </header>

    <section class="product">
      <div class="product-name">Protein:</div>
      <div class="product-variant">RECOVERY</div>
    </section>

    <section class="flavour">
      <span class="flavour-with">With</span>
      <span class="flavour-mild">Mild</span>
      <span class="flavour-name">Chocolate</span>
    </section>
  </main>
</body>
</html>
```